Web Design For Metal Recycling Company

We are a scrap and recycling company dealing mainly in scrap metal base in Singapore. We deal in both domestic market and international market. Currently we are still unsure if we want to have a "lively" or "professional" company image so we will leave it to the designer to deem what is good.

We wish for a website to be able to "Retain" the interest of new visitor and at the same time able to give enough information for new and existing customer. We would also wish for design that will get the visitor to "Engage" us.

The attached is the logo for the company and we would want to incorporate that into the website. Either of the logo is fine.

```html
<!DOCTYPE html>
<html lang="en">
<head>
<meta charset="utf-8">
<title>Tan Keng Metals Recycling</title>
<link href="https://fonts.googleapis.com/css2?family=Audiowide&family=Open+Sans:wght@400;700&display=swap" rel="stylesheet">
<style>
  :root {
    --charcoal: #333333;
    --charcoal-deep: #242222;
    --gold: #f0c312;
    --brand-gold: #c9a033;
    --white: #ffffff;
    --molten-dark: #2a160a;
    --molten-hot: #f0a030;
    --city-dark: #1d2a44;
    --city-light: #6b7fa6;
  }
  * { margin: 0; padding: 0; box-sizing: border-box; }
  html, body { width: 985px; height: 1200px; overflow: hidden; background: var(--charcoal); }
  .page { position: relative; width: 985px; height: 1200px; background: var(--charcoal); }

  .nav { position: absolute; left: 0; width: 985px; height: 50px; background: var(--charcoal); }
  .nav-top { top: 0; }
  .nav-link {
    position: absolute; transform: translateX(-50%);
    font-family: "Audiowide", sans-serif; font-size: 12px; letter-spacing: 0.5px;
    color: var(--white); text-transform: uppercase; text-decoration: none; white-space: nowrap;
  }
  .nav-top .nav-link { top: 20px; }

  .hero { position: absolute; top: 50px; left: 0; width: 985px; height: 952px; }
  .hero-art { position: absolute; inset: 0; width: 100%; height: 100%; display: block; }

  .brand {
    position: absolute; left: 46px; top: 372px; width: 300px; text-align: center;
  }
  .brand-mark {
    width: 80px; height: 80px; border: 4px solid var(--brand-gold); margin: 0 auto 22px;
  }
  .brand-name {
    font-family: "Open Sans", sans-serif; font-weight: 700; color: var(--brand-gold);
    font-size: 27px; line-height: 1.1; letter-spacing: 1px; text-transform: uppercase;
  }

  .tagline {
    position: absolute; left: 754px; top: 390px; transform: translateX(-50%);
    font-family: "Open Sans", sans-serif; font-size: 31px; color: var(--white);
    text-align: center; line-height: 63px; white-space: nowrap;
    text-shadow: 0 2px 4px rgba(0,0,0,0.6);
  }

  .footer { position: absolute; top: 1002px; left: 0; width: 985px; height: 198px; background: var(--charcoal); }
  .footer .nav-link { top: 66px; }
  .footer-brand {
    position: absolute; left: 158px; top: 108px; transform: translateX(-50%);
    display: flex; align-items: center; gap: 8px;
  }
  .footer-brand .brand-mark { width: 22px; height: 22px; border-width: 2px; margin: 0; }
  .footer-brand .brand-name { font-size: 11px; letter-spacing: 0.5px; }
  .footer-meta {
    position: absolute; top: 152px; transform: translateX(-50%);
    font-family: "Audiowide", sans-serif; font-size: 13px; color: var(--white); white-space: nowrap;
  }
</style>
</head>
<body>
<div class="page">

  <nav class="nav nav-top">
    <a class="nav-link" style="left:82px">Home</a>
    <a class="nav-link" style="left:245px">Acheivements</a>
    <a class="nav-link" style="left:409px">Services</a>
    <a class="nav-link" style="left:571px">Membership</a>
    <a class="nav-link" style="left:734px">About Us</a>
    <a class="nav-link" style="left:898px">Contact Us</a>
  </nav>

  <section class="hero">
    <svg class="hero-art" viewBox="0 42 821 793" preserveAspectRatio="none">
      <defs>
        <radialGradient id="molten" cx="0.55" cy="0.75" r="0.7">
          <stop offset="0" stop-color="#fff6d0"/>
          <stop offset="0.2" stop-color="var(--molten-hot)"/>
          <stop offset="0.6" stop-color="#7a3a12"/>
          <stop offset="1" stop-color="var(--molten-dark)"/>
        </radialGradient>
        <linearGradient id="city" x1="0" y1="0" x2="0" y2="1">
          <stop offset="0" stop-color="var(--city-light)"/>
          <stop offset="0.5" stop-color="var(--city-dark)"/>
          <stop offset="1" stop-color="#10182a"/>
        </linearGradient>
        <linearGradient id="slate" x1="0" y1="0" x2="1" y2="0">
          <stop offset="0" stop-color="#3a3838"/>
          <stop offset="1" stop-color="var(--charcoal-deep)"/>
        </linearGradient>
      </defs>
      <rect x="0" y="42" width="821" height="793" fill="var(--gold)"/>
      <polygon role="img" aria-label="Photo of molten metal pouring from a furnace ladle with sparks"
        points="0,42 440,42 821,250 821,400 450,400 0,140" fill="url(#molten)"/>
      <polygon role="img" aria-label="Photo of a waterfront city skyline at dusk"
        points="450,400 821,400 821,530 330,835 0,835 0,690" fill="url(#city)"/>
      <polygon points="0,140 455,400 0,690" fill="var(--gold)"/>
      <polygon points="0,170 420,400 0,655" fill="url(#slate)"/>
    </svg>

    <div class="brand">
      <div class="brand-mark"></div>
      <div class="brand-name">Tan Keng Metals<br>Recycling</div>
    </div>

    <h1 class="tagline">We Melt &amp; Recycle<br>the things for<br>a Brighter world</h1>
  </section>

  <footer class="footer">
    <a class="nav-link" style="left:89px">Home</a>
    <a class="nav-link" style="left:252px">Acheivements</a>
    <a class="nav-link" style="left:415px">Services</a>
    <a class="nav-link" style="left:578px">Membership</a>
    <a class="nav-link" style="left:742px">About Us</a>
    <a class="nav-link" style="left:905px">Contact Us</a>

    <div class="footer-brand">
      <div class="brand-mark"></div>
      <div class="brand-name">Tan Keng Metals<br>Recycling</div>
    </div>

    <div class="footer-meta" style="left:451px">www.tankengmetals.com</div>
    <div class="footer-meta" style="left:720px">All Rights Reserved.</div>
  </footer>

</div>
</body>
</html>
```